Playful Website Design Needed Pet Sitting and Dog Walking Business

Need a simple one page Web Design Built on WordPress.
Sections:

About Us
Services Provided
Costs
Contact Us
Intake Form (Questionnaire that goes to email)
See us in Action

Industry/Entity Type

Pet Sitting and Dog Walking

Number of Pages Required

1 page

Font styles to use
Other font styles liked:
• See the Business Card Font and use that.

Colors
EE7325
F08F49
F5BC92
FAE3D3
FDF4ED

Requirements
Must have
• See attached Logo Design, with Font's and Colors Use these as theme guide

```html
<!DOCTYPE html>
<html lang="en">
<head>
<meta charset="utf-8">
<title>Paw Pal Companions – Pet Sitting &amp; Dog Walking</title>
<link href="https://fonts.googleapis.com/css2?family=Patrick+Hand&family=Montserrat:wght@400;500;600&display=swap" rel="stylesheet">
<style>
:root{
  --teal:#137b90;
  --teal-dark:#0d6376;
  --sky:#bfeaf6;
  --sky-soft:#dff4fa;
  --orange:#ee6a1c;
  --orange-soft:#f08f49;
  --peach:#f5bc92;
  --green:#7cc520;
  --ink:#1f2a30;
  --muted:#5d666b;
  --paper:#ffffff;
  --mist:#f4f5f6;
  --hand:'Patrick Hand',cursive;
  --body:'Montserrat',sans-serif;
}
*{box-sizing:border-box;margin:0;padding:0}
html,body{width:1200px;height:4464px;overflow:hidden}
body{position:relative;background:var(--paper);font-family:var(--body);color:var(--ink)}
.abs{position:absolute}
svg.band{position:absolute;left:0;display:block}
.hand{font-family:var(--hand)}
.btn{position:absolute;display:flex;align-items:center;justify-content:center;gap:8px;background:var(--orange);color:#fff;font-family:var(--hand);font-size:19px;border-radius:30px;box-shadow:0 6px 14px rgba(238,106,28,.35)}
.btn .dot{width:13px;height:13px;border-radius:50%;background:#fff}
.photo{position:absolute}
.brand{position:absolute;font-family:var(--hand);color:var(--orange);line-height:.95;display:flex;align-items:center;gap:10px}
.brand .mark{width:34px;height:34px;border-radius:50%;background:var(--orange);flex:none}
.label{position:absolute;display:flex;align-items:center;gap:8px;font-family:var(--hand);font-size:24px;color:var(--orange)}
.label i{display:block;width:30px;height:30px;border-radius:50%;background:var(--orange);font-style:normal}
.title{position:absolute;font-family:var(--hand);font-size:50px;color:var(--ink);text-align:center;left:0;width:1200px}
.copy{font-size:13px;line-height:21px;color:var(--muted)}

/* hero */
.nav a{position:absolute;top:44px;font-family:var(--hand);font-size:19px;color:#fff;text-decoration:none}
.hero-head{position:absolute;left:182px;top:206px;font-family:var(--hand);font-size:46px;color:#fff;line-height:54px}
.hero-head .hl{display:inline-block;background:var(--green);border-radius:14px 22px 12px 20px;padding:0 16px;margin-left:-18px;transform:rotate(-2deg)}
.hero-text{position:absolute;left:182px;top:340px;font-family:var(--hand);font-size:18px;color:#fff;line-height:24px}

/* why */
.feature h3{font-family:var(--hand);font-size:28px;color:var(--orange);line-height:26px;font-weight:400}
.feature p{margin-top:14px}
.paw{position:absolute;width:52px;height:52px}

/* services */
.card{position:absolute;width:251px;height:293px;background:#fff;border-radius:24px;overflow:hidden;box-shadow:0 10px 24px rgba(0,0,0,.12);text-align:center}
.card .pic{height:156px;border-bottom:5px solid var(--green);border-radius:0 0 50% 50%/0 0 18px 18px}
.card h3{font-family:var(--hand);font-size:27px;color:var(--orange);font-weight:400;margin-top:16px}
.card p{margin:8px 22px 0;font-size:12px;line-height:20px;color:var(--muted)}

/* why us */
.gallery{position:absolute;border:6px solid #fff;border-radius:10px;box-shadow:0 8px 20px rgba(0,0,0,.15)}
.perks li{list-style:none;display:flex;align-items:center;gap:16px;font-family:var(--hand);font-size:25px;color:var(--ink);height:40px}
.perks svg{width:26px;height:26px}

/* booking */
.field{position:absolute;border-bottom:1px solid #c9ced1;font-size:10px;color:var(--muted);padding-bottom:8px}

/* footer */
.foot-links a{position:absolute;left:619px;font-family:var(--hand);font-size:21px;color:var(--teal-dark);text-decoration:none}
.social{position:absolute;top:4334px;width:17px;height:17px;border-radius:50%;background:var(--teal)}
</style>
</head>
<body>

<!-- ========== HERO ========== -->
<svg class="band" style="top:0" width="1200" height="680" viewBox="0 0 1200 680">
  <path d="M0 0H1200V560C1080 640 980 610 860 600C720 590 560 650 380 640C220 632 120 560 0 590Z" fill="var(--sky)"/>
  <path d="M0 0H1200V520C1090 600 960 580 830 575C690 570 560 630 380 618C220 606 110 540 0 560Z" fill="var(--teal)"/>
  <path d="M150 0H420C430 60 400 140 330 160C250 180 180 150 150 100C130 60 140 20 150 0Z" fill="#fff"/>
</svg>

<div class="brand" style="left:205px;top:48px;font-size:34px;flex-direction:column;align-items:flex-start;gap:0">
  <span>Paw Pal</span><span style="padding-left:26px">Companions</span>
</div>

<nav class="nav">
  <a href="#" style="left:468px">Home</a>
  <a href="#" style="left:560px">About Us</a>
  <a href="#" style="left:668px">Services</a>
  <a href="#" style="left:765px">Costs</a>
</nav>
<a class="btn" style="left:846px;top:35px;width:142px;height:46px;font-size:17px">Contact Us <span class="dot"></span></a>

<div class="photo" role="img" aria-label="Beagle on a leash beside a person's legs in a tan coat"
     style="left:590px;top:0;width:610px;height:668px;background:radial-gradient(ellipse at 40% 55%,#d9b894 0%,#b48a62 35%,rgba(19,123,144,0) 70%)"></div>

<h1 class="hero-head" style="font-weight:400">We Feed, Walk And Play With<br><span class="hl">Your Pet,</span> Each Visit!</h1>
<p class="hero-text">Lorem ipsum dolor sit amet, consectetur adipiscing elit.<br>Quam ut aliquam purus.</p>
<a class="btn" style="left:182px;top:421px;width:148px;height:46px;font-size:17px">Book A Walk <span class="dot"></span></a>

<!-- ========== WHY ========== -->
<div class="label" style="left:572px;top:710px"><i></i>Why</div>
<h2 class="title" style="top:752px;font-weight:400">Paw Pal Companions!?</h2>

<svg class="band" style="top:860px" width="1200" height="700" viewBox="0 0 1200 700" fill="none">
  <path d="M570 110C620 60 640 20 640 0M600 200C560 260 650 310 620 360M480 400C520 460 580 420 560 500C550 560 600 600 590 660" stroke="#9aa4a8" stroke-width="1.5" stroke-dasharray="5 6"/>
</svg>

<!-- feature 1 -->
<div class="photo" role="img" aria-label="Smiling woman with glasses taking a selfie"
     style="left:269px;top:841px;width:286px;height:243px;background:linear-gradient(135deg,#c9b49c,#8a6d57);border-radius:55% 45% 48% 52%/60% 50% 50% 40%;box-shadow:8px -8px 0 var(--green)"></div>
<svg class="paw" style="left:540px;top:930px" viewBox="0 0 52 52"><g fill="var(--orange)"><ellipse cx="26" cy="34" rx="12" ry="10"/><circle cx="11" cy="22" r="5.5"/><circle cx="20" cy="12" r="5.5"/><circle cx="32" cy="12" r="5.5"/><circle cx="41" cy="22" r="5.5"/></g></svg>
<div class="feature abs" style="left:664px;top:904px;width:230px">
  <h3>8$ Per Visit<br>2 Visits A Day</h3>
  <p class="copy">Lorem ipsum dolor sit amet, consectetur adipiscing elit. Quam diam ut aliquam purus.</p>
</div>

<!-- feature 2 -->
<div class="feature abs" style="left:316px;top:1138px;width:230px;text-align:right">
  <h3>All Pets, Any Age!</h3>
  <p class="copy">Lorem ipsum dolor sit amet, consectetur adipiscing elit. Quam diam ut aliquam purus.</p>
</div>
<div class="photo" role="img" aria-label="White terrier and a beagle puppy sitting on grass"
     style="left:621px;top:1092px;width:267px;height:217px;background:linear-gradient(135deg,#e6e1d6,#8f9a6a);border-radius:50% 50% 45% 55%/55% 45% 55% 45%;box-shadow:8px -8px 0 var(--green)"></div>
<svg class="paw" style="left:598px;top:1176px" viewBox="0 0 52 52"><g fill="var(--orange)"><ellipse cx="26" cy="34" rx="12" ry="10"/><circle cx="11" cy="22" r="5.5"/><circle cx="20" cy="12" r="5.5"/><circle cx="32" cy="12" r="5.5"/><circle cx="41" cy="22" r="5.5"/></g></svg>

<!-- feature 3 -->
<div class="photo" role="img" aria-label="Group of walkers with many dogs on a park path"
     style="left:248px;top:1313px;width:316px;height:234px;background:linear-gradient(135deg,#8da06a,#6b5a48);border-radius:50% 50% 45% 55%/55% 50% 50% 45%;box-shadow:8px -8px 0 var(--green)"></div>
<svg class="paw" style="left:546px;top:1408px" viewBox="0 0 52 52"><g fill="var(--orange)"><ellipse cx="26" cy="34" rx="12" ry="10"/><circle cx="11" cy="22" r="5.5"/><circle cx="20" cy="12" r="5.5"/><circle cx="32" cy="12" r="5.5"/><circle cx="41" cy="22" r="5.5"/></g></svg>
<div class="feature abs" style="left:666px;top:1408px;width:230px">
  <h3>Parent Supervised</h3>
  <p class="copy">Lorem ipsum dolor sit amet, consectetur adipiscing elit. Quam diam ut aliquam purus.</p>
</div>

<!-- ========== SERVICES ========== -->
<svg class="band" style="top:1570px" width="1200" height="1080" viewBox="0 0 1200 1080">
  <path d="M0 0C120 40 240 70 420 50C640 25 900 40 1200 10V1010C1000 1060 820 1020 600 1040C380 1060 180 1000 0 1080Z" fill="var(--sky)"/>
  <path d="M0 40C160 60 300 95 480 78C700 58 920 70 1200 40V970C1020 1000 840 980 620 1000C400 1020 180 960 0 1010Z" fill="var(--teal)"/>
</svg>

<div class="label" style="left:515px;top:1748px;color:#fff"><i></i>Services</div>
<h2 class="title" style="top:1788px;color:#fff;font-weight:400">What We Serve</h2>

<article class="card" style="left:198px;top:1869px">
  <div class="pic" role="img" aria-label="Dog resting on a pet bed" style="background:linear-gradient(160deg,#d9d5cf,#4b4a48)"></div>
  <h3>Boarding</h3>
  <p>Lorem ipsum dolor sit amet, consectetur adipiscing elit. Quam diam ut aliquam purus.</p>
</article>
<article class="card" style="left:473px;top:1869px">
  <div class="pic" role="img" aria-label="Woman sitting on the floor playing with a dog at home" style="background:linear-gradient(160deg,#eceae6,#9e8a74)"></div>
  <h3>House Sitting</h3>
  <p>Lorem ipsum dolor sit amet, consectetur adipiscing elit. Quam diam ut aliquam purus.</p>
</article>
<article class="card" style="left:751px;top:1869px">
  <div class="pic" role="img" aria-label="Dog walking on a sunlit path beside its owner" style="background:linear-gradient(160deg,#f0c77d,#7f8d4e)"></div>
  <h3>Dog Walking</h3>
  <p>Lorem ipsum dolor sit amet, consectetur adipiscing elit. Quam diam ut aliquam purus.</p>
</article>
<article class="card" style="left:331px;top:2195px">
  <div class="pic" role="img" aria-label="Woman hugging a small terrier" style="background:linear-gradient(160deg,#3f5a4a,#c9a98a)"></div>
  <h3>Doggy Day Care</h3>
  <p>Lorem ipsum dolor sit amet, consectetur adipiscing elit. Quam diam ut aliquam purus.</p>
</article>
<article class="card" style="left:607px;top:2195px">
  <div class="pic" role="img" aria-label="Pet sitter with a dog beside a parked car" style="background:linear-gradient(160deg,#c7ccd1,#8b6a46)"></div>
  <h3>Drop-In Visits</h3>
  <p>Lorem ipsum dolor sit amet, consectetur adipiscing elit. Quam diam ut aliquam purus.</p>
</article>

<!-- ========== WHY US ========== -->
<div class="label" style="left:188px;top:2762px"><i></i>Action</div>
<h2 class="abs hand" style="left:196px;top:2806px;font-size:50px;font-weight:400">Why Us?</h2>
<p class="abs" style="left:196px;top:2874px;width:276px;font-size:12.5px;line-height:23px;color:var(--muted)">Lorem Ipsum Dolor Sit Amet, Consectetur Adipiscing Elit. Quam Diam Ut Aliquam Purus. Et, Praesent Aliquet Et Non Lobortis Eget. Egestas Viverra Eu Gravida Pretium. Magna Sem Tristique Auctor Duis Et, A. Natoque Urna Quis Facilisi Risus Scelerisque Fermentum.</p>
<ul class="perks abs" style="left:200px;top:3064px">
  <li><svg viewBox="0 0 26 26" fill="none" stroke="var(--orange)" stroke-width="2"><path d="M4 22L11 15M11 15L14 8L20 4L22 10L17 14Z"/><circle cx="19" cy="19" r="3"/></svg>Trained</li>
  <li><svg viewBox="0 0 26 26" fill="none" stroke="var(--orange)" stroke-width="2"><path d="M3 14H8V23H3ZM8 15L13 10L15 4C17 4 18 6 17 9H23V14L20 22H8"/></svg>Trusted</li>
  <li><svg viewBox="0 0 26 26" fill="none" stroke="var(--orange)" stroke-width="2"><circle cx="13" cy="11" r="8"/><circle cx="13" cy="11" r="4"/><path d="M8 18L6 24L13 21L20 24L18 18"/></svg>Certified</li>
</ul>

<svg class="abs" style="left:520px;top:2840px" width="520" height="420" viewBox="0 0 520 420"><path d="M60 120C120 40 260 20 360 60C460 100 520 220 470 320C420 410 260 420 150 380C40 340 0 200 60 120Z" fill="var(--sky)"/></svg>

<div class="gallery" role="img" aria-label="Man walking several dogs in a city street" style="left:603px;top:2835px;width:155px;height:125px;background:linear-gradient(135deg,#b8a68f,#4e5c6e)"></div>
<div class="gallery" role="img" aria-label="Woman walking a pack of dogs outdoors" style="left:789px;top:2731px;width:236px;height:350px;background:linear-gradient(160deg,#c7b26a,#7b5a3e)"></div>
<div class="gallery" role="img" aria-label="Woman in a cap petting two dogs in a park" style="left:480px;top:3003px;width:255px;height:240px;background:linear-gradient(135deg,#9a8a6e,#e3ddd4)"></div>
<div class="gallery" role="img" aria-label="Close-up of a dog playing outdoors" style="left:765px;top:3102px;width:213px;height:179px;background:linear-gradient(135deg,#c9b49a,#5e4a36)"></div>

<!-- ========== CALL US ========== -->
<svg class="band" style="top:3260px" width="1200" height="960" viewBox="0 0 1200 960">
  <path d="M0 40C200 10 420 60 640 30C860 0 1040 40 1200 20V960H0Z" fill="var(--mist)"/>
  <path d="M300 580C340 520 520 500 700 505C900 510 1080 460 1200 470V960H500C380 900 260 660 300 580Z" fill="var(--sky)"/>
  <path d="M330 560C380 520 560 520 760 525C960 530 1100 480 1200 490V960H560C420 900 300 620 330 560Z" fill="var(--teal)"/>
</svg>

<div class="label" style="left:510px;top:3426px"><i></i>CALL US</div>
<h2 class="title" style="top:3468px;font-size:44px;font-weight:400">Looking For A Professional?</h2>
<p class="abs" style="left:239px;top:3533px;width:722px;font-size:12.5px;line-height:23px;color:var(--muted);text-align:center">Lorem Ipsum Dolor Sit Amet, Consectetur Adipiscing Elit. Quam Diam Ut Aliquam Purus. Et, Praesent Aliquet Et Non Lobortis Eget. Egestas Viverra Eu Gravida Pretium. Magna Sem Tristique Auctor Duis Et, A. Natoque Urna Quis Facilisi Risus Scelerisque Fermentum.</p>
<a class="btn" style="left:513px;top:3615px;width:172px;height:45px;font-size:16px">
  <svg width="14" height="14" viewBox="0 0 24 24" fill="#fff"><path d="M6.6 10.8a15.1 15.1 0 006.6 6.6l2.2-2.2a1 1 0 011-.25 11.4 11.4 0 003.6.57 1 1 0 011 1V20a1 1 0 01-1 1A17 17 0 013 4a1 1 0 011-1h3.5a1 1 0 011 1c0 1.25.2 2.45.57 3.57a1 1 0 01-.25 1z"/></svg>
  (555) 014-2290
</a>

<!-- booking card -->
<div class="abs" style="left:166px;top:3785px;width:880px;height:380px;background:#fff;border-radius:34px;box-shadow:0 12px 30px rgba(0,0,0,.12)"></div>
<div class="photo" role="img" aria-label="Woman walking two dogs along an autumn park path"
     style="left:180px;top:3799px;width:422px;height:354px;border-radius:6px;background:linear-gradient(160deg,#c9a270,#8d8a78 55%,#6a6c6e)"></div>
<div class="label" style="left:635px;top:3830px;font-size:22px"><i></i>CONTACT</div>
<h2 class="abs hand" style="left:648px;top:3858px;font-size:40px;font-weight:400">Booking Form</h2>
<svg class="abs" style="left:850px;top:3872px" width="62" height="24" viewBox="0 0 62 24" fill="none" stroke="var(--teal)" stroke-width="3" stroke-linecap="round"><path d="M4 8L58 4M10 18L50 14"/></svg>
<form>
  <div class="field" style="left:654px;top:3938px;width:158px">Name</div>
  <div class="field" style="left:834px;top:3938px;width:158px">Phone</div>
  <div class="field" style="left:654px;top:3972px;width:338px">Email</div>
  <div class="field" style="left:654px;top:4006px;width:338px;height:48px">Type Here...</div>
</form>
<a class="btn" style="left:652px;top:4080px;width:148px;height:44px;font-size:16px">Book A Walk <span class="dot"></span></a>

<!-- ========== FOOTER ========== -->
<div class="brand" style="left:153px;top:4228px;font-size:38px;flex-direction:column;align-items:flex-start;gap:0">
  <span>Paw Pal</span><span style="padding-left:30px">Companions</span>
</div>

<nav class="foot-links">
  <a href="#" style="top:4220px">About Us</a>
  <a href="#" style="top:4258px">Services</a>
  <a href="#" style="top:4295px">Costs</a>
  <a href="#" style="top:4332px">Contact Us</a>
</nav>

<div class="abs hand" style="left:822px;top:4218px;font-size:21px;color:var(--teal-dark)">Call Us</div>
<div class="abs" style="left:822px;top:4253px;display:flex;align-items:center;gap:8px;font-family:var(--hand);font-size:15px;color:var(--teal-dark)">
  <span style="width:20px;height:20px;border-radius:50%;background:var(--orange-soft);display:flex;align-items:center;justify-content:center">
    <svg width="11" height="11" viewBox="0 0 24 24" fill="#fff"><path d="M6.6 10.8a15.1 15.1 0 006.6 6.6l2.2-2.2a1 1 0 011-.25 11.4 11.4 0 003.6.57 1 1 0 011 1V20a1 1 0 01-1 1A17 17 0 013 4a1 1 0 011-1h3.5a1 1 0 011 1c0 1.25.2 2.45.57 3.57a1 1 0 01-.25 1z"/></svg>
  </span>(555) 014-2290
</div>
<div class="abs hand" style="left:822px;top:4300px;font-size:21px;color:var(--teal-dark)">Follow Us</div>
<span class="social" style="left:822px" aria-label="Social profile"></span>
<span class="social" style="left:848px" aria-label="Social profile"></span>
<span class="social" style="left:874px" aria-label="Social profile"></span>
<span class="social" style="left:904px" aria-label="Social profile"></span>

<svg class="band" style="top:4384px" width="1200" height="24" viewBox="0 0 1200 24"><path d="M150 16L1054 4L1050 18L150 18Z" fill="var(--teal-dark)"/></svg>
<p class="abs" style="left:148px;top:4428px;font-size:11px;color:var(--ink)">©Copyright 2022. <u style="color:var(--teal)">PAW PAL COMPANIONS</u> | All Rights Reserved</p>

</body>
</html>
```